Stationary Design - KM Facial Plastics

We are looking for a stylish and professional stationary design for a facial plastic surgeon. The stationary design will be for letterhead, business card, appointment cards and envelopes.
The design must be slick and aesthetically pleasing whilst incorporating the style of our logo as attached below.

Target Market(s)

Adults of all ages

Font styles to use
Serif
Script

Requirements
Must have
• Must be an aesthetically pleasing, stylish and professional design that includes the required information in a captivating layout.
• Must also be welcoming with a balanced design and a clean crisp finish.
• Details should include:
• Mr Dorian Halvet - Consultant Otolaryngologist & Facial Plastic Surgeon
• Phone: 03 5917 2846
• Fax: 03 5918 4072
• Email: info@kmfacialplastics.example.au
• Consulting from: Ashford, Brenton, Calder, Dunmore & Harbour City
• Appointment Card should include:
• Date, time, fee and location as per the attached example.
• location addresses are:
• 41 Marlow Street Echuca Vic 3564
• 318 Bramble Street Ashford Vic 3550
• Level 3, 612 Hadley Street, Epping Vic 3076
• Level 6, 480 Tennant Street Melbourne Vic 3000
Should not have
• Clutter

```html
<!DOCTYPE html>
<html lang="en">
<head>
<meta charset="UTF-8">
<title>KM Facial Plastics – Business Card</title>
<link href="https://fonts.googleapis.com/css2?family=Lato:wght@400;700;900&display=swap" rel="stylesheet">
<style>
  :root {
    --backdrop: #3b3431;
    --card: #0f1012;
    --card-edge: #1a1b1e;
    --ink: #f4f4f4;
    --ink-soft: #dcdcdc;
    --emboss: #2a2b2f;
    --rule: #d8d8d8;
  }
  * { box-sizing: border-box; margin: 0; padding: 0; }
  html, body {
    width: 1200px; height: 847px; overflow: hidden;
    background: var(--backdrop);
    font-family: "Lato", sans-serif;
  }
  .canvas {
    position: relative; width: 1200px; height: 847px;
    display: flex; align-items: center; justify-content: center; gap: 60px;
  }
  .card {
    position: relative; width: 520px; height: 318px;
    background: var(--card);
    border: 1px solid var(--card-edge);
    box-shadow: 0 14px 30px rgba(0,0,0,0.45);
  }
  .brand { display: flex; align-items: center; gap: 10px; }
  .brand-dot {
    width: 12px; height: 12px; border-radius: 50%;
    background: currentColor; flex: none;
  }
  .brand-name {
    font-weight: 400; text-transform: uppercase; letter-spacing: 1.5px;
  }
  /* back of card */
  .card-back .brand {
    position: absolute; left: 50%; top: 50%; transform: translate(-50%, -50%);
    color: var(--emboss);
  }
  .card-back .brand-name { font-size: 22px; white-space: nowrap; }
  /* front of card */
  .card-front .brand {
    position: absolute; left: 30px; top: 96px; width: 170px;
    color: var(--ink);
  }
  .card-front .brand-name { font-size: 15px; line-height: 1.35; }
  .divider {
    position: absolute; left: 214px; top: 58px; width: 1px; height: 150px;
    background: var(--rule);
  }
  .details { position: absolute; left: 236px; top: 56px; color: var(--ink); }
  .person-name { font-weight: 900; font-size: 26px; line-height: 1.05; margin-bottom: 6px; }
  .person-title { font-size: 13px; line-height: 1.3; color: var(--ink-soft); }
  .address { font-size: 13px; line-height: 1.3; margin-top: 2px; color: var(--ink-soft); }
  .contact-list { list-style: none; margin-top: 6px; }
  .contact-list li {
    display: flex; align-items: center; gap: 10px;
    font-size: 13.5px; line-height: 1.4; color: var(--ink);
  }
  .contact-list svg { width: 12px; height: 12px; flex: none; }
  .locations {
    position: absolute; left: 30px; bottom: 30px;
    font-size: 13.5px; color: var(--ink-soft); letter-spacing: 0.2px;
  }
</style>
</head>
<body>
<main class="canvas">
  <section class="card card-back" aria-label="Card back">
    <div class="brand">
      <span class="brand-dot"></span>
      <span class="brand-name">KM Facial Plastics</span>
    </div>
  </section>

  <section class="card card-front" aria-label="Card front">
    <div class="brand">
      <span class="brand-dot"></span>
      <span class="brand-name">KM Facial Plastics</span>
    </div>
    <div class="divider"></div>
    <div class="details">
      <h1 class="person-name">Mr Dorian Halvet</h1>
      <p class="person-title">Consultant Otolaryngologist &amp;<br>Facial Plastic Surgeon</p>
      <p class="address">318 Bramble Street Ashford</p>
      <ul class="contact-list">
        <li>
          <svg viewBox="0 0 24 24" aria-hidden="true"><path fill="#f4f4f4" d="M6.6 10.8a15.1 15.1 0 0 0 6.6 6.6l2.2-2.2c.3-.3.7-.4 1-.2 1.1.4 2.3.6 3.6.6.6 0 1 .4 1 1V20c0 .6-.4 1-1 1A17 17 0 0 1 3 4c0-.6.4-1 1-1h3.5c.6 0 1 .4 1 1 0 1.3.2 2.5.6 3.6.1.3 0 .7-.2 1z"/></svg>
          03 5917 2846
        </li>
        <li>
          <svg viewBox="0 0 24 24" aria-hidden="true"><path fill="#f4f4f4" d="M6 2h10l2 2v5H6zM3 10h18v9h-3v3H6v-3H3zm5 7v3h8v-3z"/></svg>
          03 5918 4072
        </li>
        <li>
          <svg viewBox="0 0 24 24" aria-hidden="true"><path fill="#f4f4f4" d="M2 5h20v14H2zm2 2v.5l8 5.5 8-5.5V7l-8 5.5z"/></svg>
          admin@halvetentclinic.example.au
        </li>
      </ul>
    </div>
    <p class="locations">Ashford, Brenton, Calder, Dunmore &amp; Harbour City</p>
  </section>
</main>
</body>
</html>
```